BKA

Please send us some options for letterhead I attached our Logo. In addition to the Logo we need this information somewhere on the page

47 Fenbury Lane
Marlow, NH 03456
203-481-7629

```html
<!DOCTYPE html>
<html lang="en">
<head>
<meta charset="utf-8">
<title>BKA Letterhead</title>
<link rel="stylesheet" href="https://fonts.googleapis.com/css2?family=Source+Sans+3:wght@400;600;700&display=swap">
<style>
  :root {
    --paper: #ffffff;
    --ink: #1f1f1f;
    --brand-dark: #3a3331;
    --footer-dark: #36302e;
    --blue-deep: #0a72c4;
    --blue-light: #6ccbe8;
    --footer-text: #ffffff;
  }
  * { margin: 0; padding: 0; box-sizing: border-box; }
  html, body {
    width: 848px;
    height: 1200px;
    overflow: hidden;
    background: var(--paper);
  }
  .letterhead {
    position: relative;
    width: 848px;
    height: 1200px;
    background: var(--paper);
    font-family: "Source Sans 3", Arial, sans-serif;
    color: var(--ink);
  }
  .decor {
    position: absolute;
    left: 0;
    top: 0;
    width: 848px;
    height: 1200px;
  }
  .brand {
    position: absolute;
    left: 20px;
    top: 22px;
    display: flex;
    align-items: center;
    gap: 16px;
  }
  .brand-mark {
    width: 66px;
    height: 66px;
    background: var(--brand-dark);
  }
  .brand-name {
    font-size: 42px;
    font-weight: 700;
    letter-spacing: 2px;
    color: var(--brand-dark);
    line-height: 1;
  }
  .address {
    position: absolute;
    left: 660px;
    top: 61px;
    font-size: 16px;
    line-height: 22px;
    color: var(--ink);
    white-space: nowrap;
  }
  .contact {
    position: absolute;
    left: 640px;
    top: 1123px;
    font-size: 14px;
    line-height: 18px;
    color: var(--footer-text);
    border-collapse: collapse;
    white-space: nowrap;
  }
  .contact td { padding: 0; }
  .contact .label { width: 62px; }
</style>
</head>
<body>
  <div class="letterhead">
    <svg class="decor" viewBox="0 0 848 1200" aria-hidden="true">
      <defs>
        <linearGradient id="header-sweep" x1="0" y1="0" x2="1" y2="0">
          <stop offset="0" stop-color="#0a72c4"/>
          <stop offset="0.45" stop-color="#6ccbe8"/>
          <stop offset="1" stop-color="#0a72c4"/>
        </linearGradient>
        <linearGradient id="rule-fade" x1="0" y1="0" x2="1" y2="0">
          <stop offset="0" stop-color="#0a72c4"/>
          <stop offset="0.6" stop-color="#6ccbe8"/>
          <stop offset="1" stop-color="#0a72c4"/>
        </linearGradient>
      </defs>
      <rect class="header-rule" x="0" y="119" width="364" height="4" fill="url(#rule-fade)"/>
      <polygon class="header-sweep" points="360,123 579,0 848,0 848,10" fill="url(#header-sweep)"/>
      <polygon class="footer-band" points="0,1167 424,1167 848,1024 848,1200 0,1200" fill="var(--footer-dark)"/>
    </svg>

    <div class="brand">
      <div class="brand-mark"></div>
      <div class="brand-name">BKA</div>
    </div>

    <div class="address">
      <div>47 Fenbury Lane,&nbsp; Marlow,</div>
      <div>NH 03456 203-481-7629</div>
    </div>

    <table class="contact">
      <tr><td class="label">Phone:</td><td>+44-7700-900415</td></tr>
      <tr><td class="label">Fax:</td><td>0161-4960327</td></tr>
      <tr><td class="label">Website:</td><td>www.bkasample.com</td></tr>
    </table>
  </div>
</body>
</html>
```